PulseRoute Tri-Fold Design & Box Layout

Need Tri-Fold Design for new brand called PulseRoute Mobile. The design should be based on colors, logo, and text copy on www.pulseroutemobile-example.com See uploads for templates to use and ask questions. I am very responsive. Also need artwork for mobile phone box to go with the flyer design concept. The box can be very generic but same color theme, etc. with logo.

Target Market(s)

all types of people but focused on the sub-prime market.

Industry/Entity Type

Wireless Communication

Font styles to use
Serif
Sans Serif

Colors
33a6d7
abd036
f78f20

Requirements
Must have
• tri-fold and box layout using provided templates. do not outline any text as we may want to update before going to print. See layout for Tri-Fold as some will be English and some Spanish. Its OK if you just duplicate the English and we will translate as needed.
Nice to have
• Colors in Logo are:
• Green - #C5D42D
• Orange - #F6941F
• Blue - #58BAE9
Should not have
• no images of people.

```html
<!DOCTYPE html>
<html lang="en">
<head>
<meta charset="utf-8">
<title>PulseRoute Mobile Tri-Fold</title>
<link href="https://fonts.googleapis.com/css2?family=Raleway:wght@300;400;600&family=Roboto:wght@400&family=Roboto+Condensed:wght@700&display=swap" rel="stylesheet">
<style>
  :root {
    --lime: #abd036;
    --orange: #f78f20;
    --blue: #33a6d7;
    --ink: #2b2b2b;
    --body-grey: #6a6a6a;
    --panel-light: #eeeeee;
    --panel-dark: #1f2022;
    --placeholder-light: #f2f2f2;
    --placeholder-mid: #d9d9d9;
    --white: #ffffff;
  }
  html, body { margin: 0; padding: 0; overflow: hidden; background: #ffffff; }
  .trifold {
    position: relative; width: 1200px; height: 574px; overflow: hidden;
    font-family: "Raleway", sans-serif;
  }
  .panel { position: absolute; top: 0; height: 574px; overflow: hidden; }

  /* Inside panel */
  .panel--features {
    left: 0; width: 397px;
    background: linear-gradient(90deg, #ffffff 0%, #f7f7f7 60%, #ececec 100%);
  }
  .feature { position: absolute; left: 54px; width: 284px; }
  .feature__title {
    margin: 0; font-weight: 400; font-size: 14.4px; letter-spacing: 0.2px;
    color: var(--ink); text-transform: uppercase; white-space: nowrap;
  }
  .feature__text {
    margin: 3px 0 0; font-weight: 300; font-size: 12.8px; line-height: 16.4px;
    color: var(--body-grey);
  }

  /* Back panel */
  .panel--contact { left: 397px; width: 397px; background: var(--panel-light); }
  .panel--contact .contact-top {
    position: absolute; left: 0; top: 0; width: 100%; height: 338px;
    background: linear-gradient(180deg, #e9eaea 0%, #ffffff 100%);
  }
  .panel--contact .lime-rule {
    position: absolute; left: 0; top: 338px; width: 100%; height: 10px; background: var(--lime);
  }
  .panel--contact .contact-base {
    position: absolute; left: 0; top: 348px; width: 100%; height: 226px;
    background: linear-gradient(180deg, #2a2b2d 0%, var(--panel-dark) 100%);
  }
  .brand {
    position: absolute; display: flex; align-items: center; gap: 10px;
    font-family: "Raleway", sans-serif; font-weight: 600; color: var(--ink);
    white-space: nowrap;
  }
  .brand__dot { width: 14px; height: 14px; border-radius: 50%; background: var(--orange); }
  .brand--contact { left: 50%; transform: translateX(-50%); top: 58px; font-size: 32px; }
  .contact-pill {
    position: absolute; left: 129px; top: 144px; width: 138px; height: 34px;
    box-sizing: border-box; border: 1.5px solid var(--lime); border-radius: 17px;
    display: flex; align-items: center; justify-content: center;
    font-family: "Roboto", sans-serif; font-size: 20px; color: var(--lime);
  }
  .contact-icons {
    position: absolute; left: 0; top: 198px; width: 100%;
    display: flex; justify-content: center; gap: 6px;
  }
  .contact-icons svg { width: 18px; height: 18px; }
  .contact-details {
    position: absolute; left: 0; top: 227px; width: 100%; margin: 0;
    text-align: center; font-family: "Roboto", sans-serif; font-style: normal;
    font-size: 15px; line-height: 18.4px; color: #111111;
  }
  .mailing-label {
    position: absolute; left: 77px; top: 381px; width: 233px; height: 137px;
    background: var(--white); border-radius: 5px;
    box-shadow: 0 6px 8px rgba(0,0,0,0.35);
  }
  .web-address {
    position: absolute; left: 0; width: 100%; text-align: center;
    font-family: "Roboto", sans-serif; font-size: 14.5px; color: var(--lime);
  }
  .panel--contact .web-address { top: 537px; }

  /* Cover panel */
  .panel--cover { left: 794px; width: 406px; background: linear-gradient(180deg, #e6e6e6 0%, #f4f4f4 100%); }
  .cover-bands { position: absolute; left: 0; top: 0; width: 406px; height: 574px; }
  .brand--cover { left: 50%; transform: translateX(-50%); top: 58px; font-size: 32px; }
  .device-photo {
    position: absolute; left: 120px; top: 128px; width: 180px; height: 300px;
    border-radius: 24px;
    background: linear-gradient(180deg, var(--placeholder-light) 0%, var(--placeholder-mid) 100%);
  }
  .cover-headline {
    position: absolute; left: 0; top: 468px; width: 100%; margin: 0; text-align: center;
    font-family: "Roboto Condensed", sans-serif; font-weight: 700;
    font-size: 26.5px; line-height: 31px; text-transform: uppercase; white-space: nowrap;
  }
  .cover-headline__lead { display: block; color: var(--orange); }
  .cover-headline__rest { display: block; color: var(--white); }
  .panel--cover .web-address { top: 538px; }
</style>
</head>
<body>
<main class="trifold">

  <section class="panel panel--features">
    <article class="feature" style="top:42px">
      <h3 class="feature__title">Simple Instant Credit Approval</h3>
      <p class="feature__text">With a 95+% approval rate, and an order which can be completed in under 5 minutes, PulseRoute gets you on track in a way other carriers can’t.</p>
    </article>
    <article class="feature" style="top:171px">
      <h3 class="feature__title">Stress Free Buying Options</h3>
      <p class="feature__text">PulseRoute takes the stress out of phone buying. We don’t require everything to be paid up front to get talking, texting, or streaming!</p>
    </article>
    <article class="feature" style="top:292px">
      <h3 class="feature__title">Get Your First Month Free</h3>
      <p class="feature__text">PulseRoute provides you with a gift card so your first month is FREE! Never settle for less, choose PulseRoute.</p>
    </article>
    <article class="feature" style="top:410px">
      <h3 class="feature__title">Best Device Protection Available</h3>
      <p class="feature__text">Ever get your brand new phone and drop it? Scratch it? Lose it? Not only do PulseRoute packages include headphones, car charger, and screen protector, they also include insurance.</p>
    </article>
  </section>

  <section class="panel panel--contact">
    <div class="contact-top"></div>
    <div class="lime-rule"></div>
    <div class="contact-base"></div>
    <div class="brand brand--contact"><span class="brand__dot"></span>PulseRoute Mobile</div>
    <div class="contact-pill">Contact Us</div>
    <div class="contact-icons" aria-hidden="true">
      <svg viewBox="0 0 18 18"><circle cx="9" cy="9" r="9" fill="#f78f20"/><path d="M9 4a3.2 3.2 0 0 0-3.2 3.2C5.8 9.6 9 13.5 9 13.5s3.2-3.9 3.2-6.3A3.2 3.2 0 0 0 9 4zm0 4.4a1.2 1.2 0 1 1 0-2.4 1.2 1.2 0 0 1 0 2.4z" fill="#fff"/></svg>
      <svg viewBox="0 0 18 18"><circle cx="9" cy="9" r="9" fill="#f78f20"/><path d="M6.3 4.5l1.5 2.2-.9 1c.6 1.2 1.4 2 2.6 2.6l1-.9 2.2 1.5-.6 1.6c-3.6-.3-6.2-2.9-6.5-6.5z" fill="#fff"/></svg>
      <svg viewBox="0 0 18 18"><circle cx="9" cy="9" r="9" fill="#f78f20"/><rect x="5" y="7" width="8" height="5" rx="1" fill="#fff"/><rect x="6.5" y="4.8" width="5" height="2.6" fill="#fff"/><rect x="6.5" y="10" width="5" height="3" fill="#f78f20"/></svg>
      <svg viewBox="0 0 18 18"><circle cx="9" cy="9" r="9" fill="#f78f20"/><rect x="4.8" y="6" width="8.4" height="6" rx="0.8" fill="#fff"/><path d="M4.8 6.3L9 9.4l4.2-3.1" fill="none" stroke="#f78f20" stroke-width="0.9"/></svg>
    </div>
    <address class="contact-details">
      2870 Maple Ridge Lane<br>
      Road, MO 654321<br>
      555.014.2280<br>
      555.014.2281<br>
      hello@pulseroute-example.com
    </address>
    <div class="mailing-label"></div>
    <div class="web-address">www.pulseroutemobile-example.com</div>
  </section>

  <section class="panel panel--cover">
    <svg class="cover-bands" viewBox="0 0 406 574" aria-hidden="true">
      <polygon points="0,108 203,210 406,108 406,574 0,574" fill="#abd036"/>
      <polygon points="0,348 203,428 406,348 406,574 0,574" fill="#1f2022"/>
    </svg>
    <div class="brand brand--cover"><span class="brand__dot"></span>PulseRoute Mobile</div>
    <div class="device-photo" role="img" aria-label="Photo of a hand holding a white smartphone with the brand name on its screen"></div>
    <h1 class="cover-headline">
      <span class="cover-headline__lead">Welcome to the New</span>
      <span class="cover-headline__rest">Age of Wireless Service!</span>
    </h1>
    <div class="web-address">www.pulseroutemobile-example.com</div>
  </section>

</main>
</body>
</html>
```